Design a menu for health restaurant

A health food restaurant in Los Angeles is seeking menu design. Our foods are made from scratch using whole ingredients.
Name: Grove Pantry
Address: 1000 E 60th StLos Angeles, CA 90347
Website: www.GrovePantry-example.com
We are looking for a clean and simple menu. Brand colors are white/tan, green and orange.

Please see attached excel with menu items and logo. We do not yet have prices.

Colors
f78f20
9bcb3c
ffffff
fff3d1

Requirements
Must have
• Easy to read.
Trifold menu design (front and back).
VEGAN, VEGETARIAN, GLUTEN FREE, CONTAINS NUTS symbols.
Logo.
Nice to have
• Incorporate brand colors, but still be easy to read.
We would like to use the Belco font (attached) if it works. If not we are open to a similar font that is easy to read.

Please see attached images.
We like the images and headers of OPTION 1. Would like something similar in trifold format.
We like the clean fonts of OPTION 2.

```html
<!DOCTYPE html>
<html lang="en">
<head>
<meta charset="utf-8">
<title>Grove Pantry – Trifold Menu</title>
<link rel="stylesheet" href="https://fonts.googleapis.com/css2?family=Montserrat:wght@400;500;600;700&display=swap">
<style>
  :root{
    --bg:#ececec;
    --paper:#ffffff;
    --ink:#231f20;
    --muted:#3d3a3b;
    --orange:#f07a22;
    --green:#2f9a3e;
    --lime:#9bcb3c;
    --gold:#c9a227;
    --brown:#9a6a2f;
    --rust:#c8643a;
    --tan:#fff3d1;
  }
  *{box-sizing:border-box;margin:0;padding:0}
  html,body{width:1200px;height:900px;overflow:hidden}
  body{background:var(--bg);font-family:"Montserrat",sans-serif;color:var(--ink);position:relative}

  .spread{position:absolute;left:35px;top:140px;width:840px;height:620px;display:flex;background:var(--paper);box-shadow:0 10px 30px rgba(0,0,0,.15)}
  .panel{position:relative;width:280px;height:620px;border-right:1px solid #e2e2e2;overflow:hidden}
  .panel:last-child{border-right:none}

  .photo-strip{height:112px;width:100%}
  .ph-bowl{background:radial-gradient(circle at 50% 50%,#c7a27a 0,#7f9a4a 35%,#f3f3f3 62%,#dcdcdc 100%)}
  .ph-salad{background:radial-gradient(circle at 50% 50%,#c0394a 0,#5d8a3a 38%,#f3f3f3 64%,#d9d9d9 100%)}
  .ph-salmon{background:radial-gradient(circle at 50% 50%,#f08a4b 0,#7da54a 40%,#f3f3f3 64%,#dadada 100%)}

  .cols{display:flex;gap:10px;padding:12px 12px 0}
  .col{flex:1;min-width:0}

  .section-title{font-size:8.5px;font-weight:500;letter-spacing:.6px;text-transform:uppercase;padding-bottom:3px;border-bottom:2px solid var(--brown);margin:0 0 6px}
  .t-bowls{border-color:var(--brown)}
  .t-soups{border-color:var(--lime)}
  .t-wraps{border-color:var(--orange)}
  .t-salad{border-color:var(--green)}
  .t-burgers{border-color:var(--rust)}
  .t-snacks{border-color:var(--rust)}
  .t-combos{border-color:var(--lime)}

  .item{margin-bottom:7px}
  .item-name{font-size:7.4px;font-weight:700;line-height:1.2}
  .item-name .price{font-weight:500;margin-left:2px}
  .item-desc{font-size:6.2px;line-height:1.3;color:var(--muted)}
  .tag{display:inline-block;width:5px;height:5px;border-radius:50%;margin-left:2px;vertical-align:middle}
  .tag.gf{background:var(--gold)}
  .tag.vg{background:var(--green)}
  .tag.veg{background:var(--lime)}
  .tag.nut{background:var(--orange)}

  .soup-photo{width:78px;height:78px;border-radius:50%;margin:6px auto 8px;background:radial-gradient(circle,#c98a1e 0,#d89a2c 55%,#f4f4f4 70%,#e3e3e3 100%)}
  .side-photo{width:112px;height:92px;border-radius:50%;margin:6px auto 0;background:radial-gradient(circle,#c0394a 0,#6f9a3e 45%,#f5f5f5 66%,#e3e3e3 100%)}

  .legend{position:absolute;left:12px;bottom:10px;display:flex;gap:9px;font-size:5.5px;text-transform:uppercase;letter-spacing:.3px;color:var(--muted)}
  .legend span{display:flex;align-items:center;gap:3px}
  .legend .tag{width:7px;height:7px;margin:0}

  .bottom-photo{position:absolute;left:0;right:0;bottom:0;height:240px;background:linear-gradient(160deg,#f6f6f6 0,#e9e9e6 30%,#b9c98a 55%,#6b9a46 75%,#c05a6a 100%)}
  .smoothie-photo{position:absolute;left:0;bottom:0;width:100px;height:150px;background:linear-gradient(180deg,#fafafa 0,#9bc24a 40%,#7aa734 100%)}

  .cover{position:absolute;left:905px;top:140px;width:260px;height:620px;box-shadow:0 10px 30px rgba(0,0,0,.15);overflow:hidden}
  .cover-bg{position:absolute;inset:0;background:linear-gradient(180deg,#f3f2ef 0,#fbfbfa 30%,#fbfbfa 70%,#efeeeb 100%)}
  .cover-food-top,.cover-food-bottom{position:absolute;left:0;right:0;height:110px}
  .cover-food-top{top:0;background:linear-gradient(90deg,#f0c36a 0,#f8f6f2 45%,#f8f6f2 70%,#d6a24e 100%)}
  .cover-food-bottom{bottom:0;background:linear-gradient(90deg,#e3d2b0 0,#f8f6f2 40%,#f8f6f2 60%,#e2bf8e 100%)}
  .brand{position:absolute;left:0;right:0;top:238px;display:flex;flex-direction:column;align-items:center;gap:12px}
  .brand-mark{width:74px;height:74px;border-radius:50%;background:var(--orange)}
  .brand-name{font-size:22px;font-weight:500;color:var(--orange);letter-spacing:1px;text-transform:uppercase}
  .address{position:absolute;left:0;right:0;top:372px;text-align:center;font-size:8.5px;font-weight:500;color:var(--green);line-height:1.45}
  .web{position:absolute;left:0;right:0;top:412px;text-align:center;font-size:10px;font-weight:600;color:var(--orange)}
</style>
</head>
<body>

<main class="spread">
  <section class="panel">
    <div class="photo-strip ph-bowl" role="img" aria-label="Southwest bowl with grilled chicken, avocado and black beans"></div>
    <div class="cols">
      <div class="col">
        <h2 class="section-title t-bowls">Bowls</h2>
        <div class="item"><p class="item-name">Southwest Bowl <span class="price">XX</span><i class="tag gf"></i></p><p class="item-desc">Your choice of protein with corn, black beans, red onions, almonds and avocado over quinoa with lime hot sauce.</p></div>
        <div class="item"><p class="item-name">Chimi Bowl <span class="price">XX</span><i class="tag gf"></i></p><p class="item-desc">Your choice of protein with red bell pepper, mushrooms, zucchini, squash, onion, cherry tomatoes and fresh herb chimichurri on wild and brown rice.</p></div>
        <div class="item"><p class="item-name">Soba Noodle Bowl <span class="price">XX</span></p><p class="item-desc">Your choice of protein with spinach, snow peas, roasted carrots, red bell pepper, cilantro, sesame seeds and ginger lime sauce over soba noodles.</p></div>
        <div class="item"><p class="item-name">Hollywood Bowl <span class="price">XX</span><i class="tag gf"></i></p><p class="item-desc">Your choice of protein with broccoli, roasted corn, cherry tomatoes, basil, pepitas, flax seeds and lemon juice on wild and brown rice.</p></div>
        <div class="item"><p class="item-name">Grove Bowl <span class="price">XX</span><i class="tag gf"></i></p><p class="item-desc">Your choice of protein with roasted chickpeas and cauliflower, zesty fennel salad and citrus yogurt.</p></div>
        <div class="item"><p class="item-name">Buddha Bowl <span class="price">XX</span></p><p class="item-desc">Your choice of protein with corn, red kale, sweet potatoes, red cabbage, parsley, oregano, hummus, and farro.</p></div>
        <div class="item"><p class="item-name">Chili Rice Bowl <span class="price">XX</span><i class="tag gf"></i></p><p class="item-desc">Chicken, onions, bell peppers, jalapeños, black &amp; kidney beans, and tomato over brown rice.</p></div>
      </div>
      <div class="col">
        <h2 class="section-title t-soups">Soups</h2>
        <div class="item"><p class="item-name">Chicken Noodle <span class="price">XX</span></p><p class="item-desc">Chicken, egg noodles, root vegetables, oregano &amp; peppercorns.</p></div>
        <div class="item"><p class="item-name">Grove Chili <span class="price">XX</span><i class="tag gf"></i></p><p class="item-desc">Chicken, onions, bell peppers, jalapeños, black &amp; kidney beans, and tomato.</p></div>
        <div class="item"><p class="item-name">Seasonal Rotating <span class="price">XX</span><i class="tag vg"></i></p><p class="item-desc">(Butternut Squash Soup V+, GF) Butternut squash blended with warm spices, and coconut milk.</p></div>
        <div class="soup-photo" role="img" aria-label="Bowl of butternut squash soup"></div>
        <h2 class="section-title t-wraps">Wraps</h2>
        <div class="item"><p class="item-name">Rancher's Wrap <span class="price">XX</span></p><p class="item-desc">Tomato, red onion, hard boiled egg, avocado, feta cheese, microgreens, romaine, grilled chicken and ranch dressing in a grilled wrap.</p></div>
        <div class="item"><p class="item-name">Vegan Tuna Wrap <span class="price">XX</span><i class="tag vg"></i></p><p class="item-desc">Vegan tuna, romaine, avocado, celery, shallot, and oregano with Meadowleaf Sauce in a whole grain wrap.</p></div>
        <div class="item"><p class="item-name">Vegetarian Wrap <span class="price">XX</span><i class="tag veg"></i></p><p class="item-desc">Roasted chickpeas, romaine, avocado, red bell pepper, shaved carrots, cucumber, spinach, basil, black beans and feta with lemon-hummus in a sprouted 7-grain wrap.</p></div>
      </div>
    </div>
    <div class="legend">
      <span><i class="tag gf"></i>Gluten free</span>
      <span><i class="tag vg"></i>Vegan</span>
      <span><i class="tag veg"></i>Vegetarian</span>
      <span><i class="tag nut"></i>Contains nuts</span>
    </div>
  </section>

  <section class="panel">
    <div class="photo-strip ph-salad" role="img" aria-label="Mixed green salad with strawberries, avocado and feta"></div>
    <div class="cols">
      <div class="col">
        <h2 class="section-title t-salad">Salad</h2>
        <div class="item"><p class="item-name">Avocado, Golden Beet, and Cranberry Salad <span class="price">XX</span><i class="tag vg"></i></p><p class="item-desc">Gold beets, avocado, dried cranberries, watermelon radish, red kale, romaine, mixed greens, and pepitas served with Golden Sun dressing.</p></div>
        <div class="item"><p class="item-name">Burrata Salad <span class="price">XX</span><i class="tag veg"></i></p><p class="item-desc">Tomato, melon, shredded basil, balsamic glaze, fresh cracked pepper, and olive oil with burrata.</p></div>
        <div class="item"><p class="item-name">Mediterranean Salad <span class="price">XX</span><i class="tag gf"></i></p><p class="item-desc">Cucumbers, Kalamata olives, cherry tomatoes, parsley, tricolor quinoa, hard-boiled egg, and hummus on mixed greens, romaine, and red cabbage with lemon-olive oil dressing.</p></div>
        <div class="item"><p class="item-name">Vegan Chef Salad <span class="price">XX</span><i class="tag vg"></i><i class="tag nut"></i></p><p class="item-desc">Roasted potatoes and carrots, chickpeas, avocado, microgreens and walnuts on mixed greens, romaine, and red kale with vegan ranch.</p></div>
        <div class="item"><p class="item-name">Rancher's Salad <span class="price">XX</span><i class="tag gf"></i></p><p class="item-desc">Tomato, red onion, hard boiled egg, avocado, feta cheese, microgreens, and grilled chicken on romaine with Ranch dressing.</p></div>
      </div>
      <div class="col">
        <h2 class="section-title t-burgers">Burgers n' Sammies</h2>
        <div class="item"><p class="item-name">Air Fried Chicken Sammy <span class="price">XX</span></p><p class="item-desc">Air fried chicken breast topped with red leaf lettuce, tomato, house made pickles and Grove Sauce on a bun served with choice of salad or fries.</p></div>
        <div class="item"><p class="item-name">Grilled Chicken Sammy <span class="price">XX</span></p><p class="item-desc">Grilled chicken topped with guacamole, red leaf lettuce, tomato, house made pickles and Grove Sauce. Served with regular fries or side salad.</p></div>
        <div class="item"><p class="item-name">Classic Beef Burger <span class="price">XX</span></p><p class="item-desc">House seasoned beef burger topped with red leaf lettuce, tomato, cheddar cheese, house made pickles and Grove Sauce on a bun served with choice of salad or fries.</p></div>
        <div class="item"><p class="item-name">Black Bean Pine Nut Burger <span class="price">XX</span><i class="tag nut"></i></p><p class="item-desc">House made black bean pine nut burger topped with red leaf lettuce, tomato, house made pickles and mustard aioli on a bun served with choice of salad or fries.</p></div>
        <div class="item"><p class="item-name">Salmon Burger <span class="price">XX</span></p><p class="item-desc">House made salmon burger topped with red leaf lettuce, tomato, house made pickles and Grove yogurt on a bun served with choice of salad or fries.</p></div>
        <div class="side-photo" role="img" aria-label="Green salad with strawberries and feta"></div>
      </div>
    </div>
  </section>

  <section class="panel">
    <div class="photo-strip ph-salmon" role="img" aria-label="Salmon plate, burger with fries and avocado toast"></div>
    <div class="cols">
      <div class="col">
        <h2 class="section-title t-snacks">Snacks n' Sides</h2>
        <div class="item"><p class="item-name">Fries <span class="price">XX</span><i class="tag vg"></i></p><p class="item-desc">Hand cut air-fries with house seasonings. Choose regular or sweet potato fries.</p></div>
        <div class="item"><p class="item-name">Side Salad <span class="price">XX</span></p><p class="item-desc">Your choice of House, Golden Beet, Mediterranean, or Vegan Chef side salad. (24oz)</p></div>
        <div class="item"><p class="item-name">Guac + Chips <span class="price">XX</span><i class="tag vg"></i></p><p class="item-desc">Guacamole with blue corn tortilla chips.</p></div>
        <div class="item"><p class="item-name">Hummus + Chips <span class="price">XX</span><i class="tag vg"></i></p><p class="item-desc">Hummus with blue corn tortilla chips.</p></div>
      </div>
      <div class="col">
        <h2 class="section-title t-combos">Combos</h2>
        <div class="item"><p class="item-name">Soup + Salad <span class="price">XX</span></p><p class="item-desc">Your choice of soup and side salad. 16oz soup + 38oz salad</p></div>
        <div class="item"><p class="item-name">Avo Toast Combo <span class="price">XX</span></p><p class="item-desc">Half avocado toast and your choice of soup. 16oz</p></div>
        <div class="item"><p class="item-name">Soup + Sammy <span class="price">XX</span></p><p class="item-desc">Your choice of soup and sandwich. 16oz soup + Sandwich</p></div>
      </div>
    </div>
    <div class="bottom-photo" role="img" aria-label="Burger with fries, salmon bowl and beet salad with avocado"></div>
    <div class="smoothie-photo" role="img" aria-label="Green smoothie in a glass"></div>
  </section>
</main>

<section class="cover">
  <div class="cover-bg" role="img" aria-label="White painted wood boards"></div>
  <div class="cover-food-top" role="img" aria-label="Breakfast dishes and herbs along the top edge"></div>
  <div class="cover-food-bottom" role="img" aria-label="Flatbread, dips and vegetables along the bottom edge"></div>
  <div class="brand">
    <div class="brand-mark"></div>
    <h1 class="brand-name">Grove Pantry</h1>
  </div>
  <p class="address">2417 W 38th Ave<br>Los Angeles, CA 90347</p>
  <p class="web">www.GrovePantry-example.com</p>
</section>

</body>
</html>
```